PowerPoint Design Process Flow for Rare Disease Patient Registries

I have attached a powerpoint presentation I need professional design on. This describes our BRIDGEWAY program and the current process and screenshots are include in the attached file. We would like to keep the process, flow, screenshots and images but need it designed to be more visually appealing while stepping through the process.
Looking for a visual queue that let's the user know what step in the process we are on as we then describe the details of that step. We want to reinforce the 5 steps in the process and keep that on each slide. Suggestions on the initial page where we introduce the process before going into the details.
I have attached an image of a button that we will be using for registration buttons and if you could reflect that kind of shape or look and feel that would be cool. Please check http://www.carepathwaylane.example to see our colors.
Target Market(s)
patient advocacy organizations that represent rare disease communities. Pharmaceutical companies that sell treatments into the disease community.
Industry/Entity Type
It Professional
Look and feel

```html
<!DOCTYPE html>
<html lang="en">
<head>
<meta charset="utf-8">
<title>Registry Partners Control Branding and Messaging</title>
<link href="https://fonts.googleapis.com/css2?family=Exo+2:ital,wght@0,400;0,500;0,600;1,700&family=Arimo:wght@400;700&display=swap" rel="stylesheet">
<style>
:root{
  --page:#ececec;
  --navy:#1f5078;
  --green:#6aab2a;
  --red:#b90e25;
  --red-dark:#8f0a1c;
  --ink:#3a3a3a;
  --grey-tab:#7a7a7a;
  --grey-tab-dark:#555;
  --screen-edge:#8ea8e4;
  --screen-bar:#c9c9c9;
  --field:#fbf6b4;
  --link:#2159c9;
  --button:#2a62d6;
}
*{box-sizing:border-box;margin:0;padding:0}
html,body{width:1200px;height:1000px;overflow:hidden}
body{background:var(--page);font-family:"Exo 2",sans-serif;position:relative}

.slide{
  position:absolute;left:33px;top:76px;width:708px;height:530px;
  transform:scale(1.6);transform-origin:top left;
  background:#fff;overflow:hidden;
}
.slide__header{position:absolute;left:0;top:0;width:100%;height:46px;background:var(--navy);border-bottom:2px solid var(--green)}
.process-nav{position:absolute;top:21px;left:54px;display:flex;gap:10px}
.process-step{position:relative;width:112px;height:34px}
.process-step svg{position:absolute;inset:0}
.process-step span{position:absolute;left:0;right:10px;top:7px;text-align:center;font-style:italic;font-weight:700;font-size:13px;letter-spacing:.5px;color:#e8e8e8}
.process-step--active span{color:#fff}

.headline{position:absolute;left:52px;top:115px;color:var(--ink)}
.headline__kicker{font-size:20px;font-weight:500;letter-spacing:.6px;line-height:1}
.headline__main{font-size:63px;font-weight:600;color:var(--red);line-height:1;margin:4px 0 2px -2px;letter-spacing:1px}
.headline__tail{font-size:20px;font-weight:500;letter-spacing:.6px;line-height:1}

.band{position:absolute;background:var(--red)}
.band--upper{left:619px;top:130px;width:89px;height:89px}
.band--lower{left:0;top:331px;width:708px;height:88px}

.screen{
  position:absolute;background:#fff;display:flex;flex-direction:column;
  border-left:6px solid var(--screen-edge);border-right:6px solid var(--screen-edge);
  box-shadow:0 4px 10px rgba(0,0,0,.45);font-family:Arimo,sans-serif;color:#333;
}
.screen--clearview{left:370px;top:84px;width:251px;height:175px}
.screen--renal{left:53px;top:273px;width:285px;height:204px}
.screen--bright{left:415px;top:280px;width:239px;height:169px}

.screen__login{display:flex;justify-content:flex-end;align-items:center;gap:3px;height:14px;padding:0 4px;font-size:3.6px;background:#fafafa}
.screen__login i{display:inline-block;width:22px;height:5px;background:var(--field);font-style:normal;padding-left:1px;line-height:5px}
.screen__login b{font-weight:400;border:.5px solid #aaa;padding:0 1.5px;background:#eee}
.screen__login a{color:var(--link);text-decoration:none}
.screen__nav{display:flex;height:9px;background:linear-gradient(#e4e4e4,var(--screen-bar));font-size:3.4px;align-items:stretch}
.screen__nav span{padding:0 4px;display:flex;align-items:center}
.screen__nav .is-current{background:var(--button);color:#fff}
.screen__body{flex:1;display:flex;gap:5px;padding:5px;background:#f1f1f1}
.screen__aside{width:29%;background:#fff;padding:3px;font-size:3.3px;line-height:1.35}
.screen__brand{display:flex;align-items:center;gap:2px;font-family:"Exo 2",sans-serif;font-weight:600;color:var(--navy);font-size:6px;padding:4px 0 6px}
.screen__brand::before{content:"";width:6px;height:6px;border-radius:50%;background:var(--green);flex:none}
.screen__aside h3{font-size:5px;margin:2px 0 3px}
.screen__aside a{color:var(--link)}
.screen__main{flex:1;background:#fff;padding:4px;font-size:3.3px;line-height:1.35}
.screen__photo{width:100%;margin-bottom:4px}
.screen__cta{display:block;width:48%;margin:0 auto 4px;background:var(--button);color:#fff;text-align:center;font-size:3.4px;font-weight:700;padding:1px 0}

.photo--family{height:64%;background:linear-gradient(180deg,#3a86d4 0%,#9cc8ee 45%,#d6c6b4 60%,#6ca82a 100%)}
.photo--elders{height:58%;background:linear-gradient(120deg,#e9e6e1 0%,#cdb9a5 45%,#a6b9c9 75%,#ecebe8 100%)}
.photo--lab{height:60%;background:linear-gradient(135deg,#dbe9f1 0%,#8fb7cf 45%,#f1eee9 70%,#a9c3d6 100%)}

.brand-mark{position:absolute;left:439px;top:484px;display:flex;align-items:center;gap:7px;font-family:"Exo 2",sans-serif;font-size:17px;font-weight:500;letter-spacing:2.5px;color:#6e6e6e}
.brand-mark::before{content:"";width:14px;height:14px;border-radius:50%;background:#3a8fd2}
.slide__footer{position:absolute;left:0;bottom:0;width:100%;height:11px;background:var(--green)}
</style>
</head>
<body>
<main class="slide">
  <header class="slide__header">
    <nav class="process-nav">
      <div class="process-step process-step--active">
        <svg viewBox="0 0 112 34" width="112" height="34"><path d="M2 3 H108 L100 31 H8 Z" fill="var(--red)" stroke="var(--red-dark)"/></svg>
        <span>PROMOTE</span>
      </div>
      <div class="process-step">
        <svg viewBox="0 0 112 34" width="112" height="34"><path d="M2 3 H108 L100 31 H8 Z" fill="var(--grey-tab)" stroke="var(--grey-tab-dark)"/></svg>
        <span>COLLECT</span>
      </div>
      <div class="process-step">
        <svg viewBox="0 0 112 34" width="112" height="34"><path d="M2 3 H108 L100 31 H8 Z" fill="var(--grey-tab)" stroke="var(--grey-tab-dark)"/></svg>
        <span>EXTEND</span>
      </div>
      <div class="process-step">
        <svg viewBox="0 0 112 34" width="112" height="34"><path d="M2 3 H108 L100 31 H8 Z" fill="var(--grey-tab)" stroke="var(--grey-tab-dark)"/></svg>
        <span>SHARE</span>
      </div>
      <div class="process-step">
        <svg viewBox="0 0 112 34" width="112" height="34"><path d="M2 3 H108 L100 31 H8 Z" fill="var(--grey-tab)" stroke="var(--grey-tab-dark)"/></svg>
        <span>BRIDGEWAY</span>
      </div>
    </nav>
  </header>

  <h1 class="headline">
    <div class="headline__kicker">REGISTRY PARTNERS</div>
    <div class="headline__main">CONTROL</div>
    <div class="headline__tail">BRANDING AND MESSAGING</div>
  </h1>

  <div class="band band--upper"></div>
  <div class="band band--lower"></div>

  <section class="screen screen--clearview">
    <div class="screen__login">Username <i>admin</i> Password <i>•••••</i> <b>Login</b> <a>Forgot login?</a></div>
    <div class="screen__nav"><span class="is-current">Home</span><span>Contact Us</span><span>Register</span></div>
    <div class="screen__body">
      <aside class="screen__aside">
        <div class="screen__brand">Clearview</div>
        <h3>The Clearview Foundation</h3>
        <p>Many people living with chronic pressure headaches face daily symptoms that change how they work, rest and plan. Our mission is to advocate, support and raise awareness together.</p>
      </aside>
      <div class="screen__main">
        <div class="screen__photo photo--family" role="img" aria-label="Photo of a family relaxing together on a grassy lawn"></div>
        <span class="screen__cta">Click here to register now!</span>
        <p>Welcome to the foundation registry. Your participation helps researchers and clinicians understand symptoms and improve care for people with this condition.</p>
      </div>
    </div>
  </section>

  <section class="screen screen--renal">
    <div class="screen__login">Username <i>admin</i> Password <i>•••••</i> <b>Login</b> <a>Forgot login?</a></div>
    <div class="screen__nav"><span class="is-current">Home</span><span>Contact Us</span><span>Register</span></div>
    <div class="screen__body">
      <aside class="screen__aside">
        <div class="screen__brand">RenalHope.example</div>
        <h3>About Us</h3>
        <p>The association is the largest patient led organization dedicated to ending suffering from renal cancers. Learn how we help patients and medical professionals at <a>www.renalhope.example</a></p>
      </aside>
      <div class="screen__main">
        <div class="screen__photo photo--elders" role="img" aria-label="Photo of three generations of a family sitting together indoors"></div>
        <span class="screen__cta">Click here to register now!</span>
        <p>By working together and sharing information, we can transform medicine in ways that were unimaginable a decade ago. Your participation may result in speeding therapies from the bench to the bedside, while rapidly increasing our knowledge of disease processes.</p>
      </div>
    </div>
  </section>

  <section class="screen screen--bright">
    <div class="screen__login">Username <i>admin</i> Password <i>•••••</i> <b>Login</b> <a>Forgot login?</a></div>
    <div class="screen__nav"><span class="is-current">Home</span><span>Contact Us</span><span>Register</span></div>
    <div class="screen__body">
      <aside class="screen__aside">
        <div class="screen__brand">Bright Steps</div>
        <h3>Bright Steps Family Registry: Stronger Side by Side</h3>
        <p>Hope and treatment are growing, and the registry is here to help families share data sooner.</p>
      </aside>
      <div class="screen__main">
        <div class="screen__photo photo--lab" role="img" aria-label="Photo of a researcher working with test tubes in a laboratory"></div>
        <span class="screen__cta">Click here to register now!</span>
        <p>Scientific advancements for treatments are moving at a steady pace. Now is the time for us to come together and share data in one registry.</p>
      </div>
    </div>
  </section>

  <div class="brand-mark">CAREPATHWAY LANE</div>
  <div class="slide__footer"></div>
</main>
</body>
</html>
```